Graphic for Spirits / Liquor Brand

Graphic of 750 ml spirits bottle that evokes bold, spooky images of the Civil War. I envision a floating spirit or spirits coming off of the bottle. Image should be scalable / vector in transparent background. Brand 'Lantern Hollow' can be shown on bottle label or around bottle. Beverages are limited edition for the upscale market. Use civil war and beverage imagery that is open source or is original artwork. Provide names / types of fonts and colts used in design.
Target Market(s)
Sophisticated Adults who enjoy premium beverages

```html
<!DOCTYPE html>
<html lang="en">
<head>
<meta charset="utf-8">
<title>Lantern Hollow Whiskey</title>
<link rel="stylesheet" href="https://fonts.googleapis.com/css2?family=Sancreek&family=Roboto+Slab:wght@400;700&family=Oswald:wght@400&display=swap">
<style>
  :root {
    --bg-dark: #1c1c1c;
    --smoke: #cfcfcf;
    --label: #2e2a26;
    --label-deep: #24211e;
    --gold: #d9cfaa;
    --gold-soft: #bdb38f;
    --amber-light: #f0b77c;
    --amber: #d98f45;
    --amber-deep: #9c5a22;
    --cap: #8d8d8d;
  }
  html, body { margin: 0; padding: 0; overflow: hidden; }
  body { width: 1200px; height: 1200px; background: var(--bg-dark); }
  .canvas { position: relative; width: 1200px; height: 1200px; overflow: hidden; }
  .smoke-scene {
    position: absolute; inset: 0;
    background:
      radial-gradient(ellipse 380px 300px at 600px 420px, rgba(230,230,230,.85), rgba(230,230,230,0) 70%),
      radial-gradient(ellipse 300px 260px at 220px 560px, rgba(200,200,200,.55), rgba(200,200,200,0) 70%),
      radial-gradient(ellipse 340px 260px at 900px 950px, rgba(190,190,190,.45), rgba(190,190,190,0) 70%),
      radial-gradient(ellipse 300px 220px at 250px 1000px, rgba(170,170,170,.4), rgba(170,170,170,0) 70%),
      linear-gradient(180deg, #2a2a2a, #151515);
  }
  .soldier-art {
    position: absolute; left: 824px; top: 120px; width: 360px; height: 600px;
    background: radial-gradient(ellipse at 45% 45%, rgba(20,20,20,.85), rgba(20,20,20,0) 70%);
  }
  .bottle { position: absolute; inset: 0; }
  .label-text { font-family: "Roboto Slab", serif; fill: var(--gold); }
  .brand-title { font-family: "Sancreek", serif; font-size: 56px; fill: var(--gold); letter-spacing: 1px; }
  .variety { font-family: "Oswald", sans-serif; font-size: 32px; fill: var(--gold); letter-spacing: 10px; }
</style>
</head>
<body>
<div class="canvas">
  <div class="smoke-scene" role="img" aria-label="Grey battlefield smoke drifting around the bottle"></div>
  <div class="soldier-art" role="img" aria-label="Dark painted illustration of a marching soldier in the smoke"></div>

  <svg class="bottle" width="1200" height="1200" viewBox="0 0 1200 1200">
    <defs>
      <linearGradient id="amberFill" x1="0" x2="1" y1="0" y2="0">
        <stop offset="0" stop-color="var(--amber-deep)"/>
        <stop offset=".2" stop-color="var(--amber)"/>
        <stop offset=".5" stop-color="var(--amber-light)"/>
        <stop offset=".8" stop-color="var(--amber)"/>
        <stop offset="1" stop-color="var(--amber-deep)"/>
      </linearGradient>
      <linearGradient id="capFill" x1="0" x2="1">
        <stop offset="0" stop-color="#6d6d6d"/>
        <stop offset=".5" stop-color="#b4b4b4"/>
        <stop offset="1" stop-color="#5e5e5e"/>
      </linearGradient>
    </defs>

    <!-- neck -->
    <rect class="neck-glass" x="524" y="200" width="148" height="140" fill="rgba(220,220,220,.35)" stroke="rgba(255,255,255,.5)"/>
    <rect class="cork" x="538" y="216" width="120" height="100" fill="#b9a88a" role="img" aria-label="Cork stopper"/>
    <!-- cap -->
    <rect class="cap" x="502" y="156" width="176" height="54" rx="6" fill="url(#capFill)"/>

    <!-- body -->
    <path class="bottle-body" d="M372,420 Q372,338 456,336 L744,336 Q828,338 828,420 L828,1050 Q828,1068 808,1068 L392,1068 Q372,1068 372,1050 Z" fill="url(#amberFill)" stroke="rgba(255,255,255,.4)" stroke-width="2"/>
    <ellipse cx="600" cy="700" rx="180" ry="300" fill="rgba(255,235,210,.18)"/>

    <!-- label -->
    <g class="label">
      <rect x="376" y="532" width="448" height="348" fill="var(--label)" opacity=".95"/>
      <rect x="376" y="812" width="448" height="60" fill="#3a352f" role="img" aria-label="Engraved battle scene strip"/>
      <g stroke="var(--gold-soft)" stroke-width="1.5">
        <line x1="392" y1="588" x2="528" y2="588"/><line x1="672" y1="588" x2="808" y2="588"/>
        <line x1="392" y1="596" x2="528" y2="596"/><line x1="672" y1="596" x2="808" y2="596"/>
        <line x1="392" y1="668" x2="808" y2="668"/>
        <line x1="392" y1="760" x2="808" y2="760"/>
        <line x1="400" y1="794" x2="500" y2="794"/><line x1="700" y1="794" x2="800" y2="794"/>
        <line x1="392" y1="838" x2="808" y2="838"/>
      </g>
      <circle cx="604" cy="576" r="76" fill="var(--label-deep)" stroke="var(--gold-soft)" stroke-width="2"/>
      <circle cx="604" cy="576" r="66" fill="#c8bfa0" role="img" aria-label="Engraved portrait of a Civil War officer"/>

      <text class="label-text" x="520" y="614" font-size="16" text-anchor="middle">MM</text>
      <text class="label-text" x="700" y="614" font-size="16" text-anchor="middle">XVI</text>
      <text class="label-text" x="478" y="650" font-size="19" font-weight="700" text-anchor="middle">PREMIUM</text>
      <text class="label-text" x="718" y="650" font-size="19" font-weight="700" text-anchor="middle">QUALITY</text>
      <text class="brand-title" x="600" y="744" text-anchor="middle" textLength="420" lengthAdjust="spacingAndGlyphs">LANTERN HOLLOW</text>
      <text class="variety" x="604" y="806" text-anchor="middle">WHISKEY</text>
      <text class="label-text" x="600" y="832" font-size="12" font-weight="700" text-anchor="middle">750 ml</text>
      <text class="label-text" x="604" y="858" font-size="14" letter-spacing="3" text-anchor="middle">MAUFACTURED IN THE USA</text>
    </g>
  </svg>
</div>
</body>
</html>
```